Brenvick Holdings LLC, new Business cards

I'm moving offices and need new cards. Plus I'm open to modifying the current design of my card. I will keep the logo but would like to explore other layouts and fonts for the design. I've included the current double sided card for reference. I Like the navy color and white. Might be open to grays or silver. Needs to be clean and elegant.

Target Market(s)

Investors, buyers & sellers of private equities and real estate.

Contact Information for Business Card

Brenvick Holdings
Dorian P.K. Halvers, Managing Principal
418 Ostrander Ave., Suite 612
Denver, CO 80319
M: 970-555-0147, O: 303-555-0192
Dorian@brenvickholdings.example
Brenvickholdings.example

Colors
0354a2
ffffff
c4c4c4

Requirements
Must have
• Business card details.
• Logo raised or embossed, it was designed after a wax seal. Current has raised ink.
Nice to have
• Space on card to write additional notes.

```html
<!DOCTYPE html>
<html lang="en">
<head>
<meta charset="utf-8">
<title>Brenvick Holdings – Business Card</title>
<link rel="stylesheet" href="https://fonts.googleapis.com/css2?family=Source+Sans+3:wght@400;700&display=swap">
<style>
  :root {
    --navy: #1f1b55;
    --paper: #f7f6f4;
    --ink: #55526e;
    --backdrop: #e9e7e3;
    --mark: #ffffff;
  }
  * { box-sizing: border-box; margin: 0; padding: 0; }
  html, body { width: 1200px; height: 800px; overflow: hidden; }
  body {
    background: var(--backdrop);
    font-family: "Source Sans 3", "Helvetica Neue", Arial, sans-serif;
    position: relative;
  }
  .card {
    position: absolute;
    top: 252px;
    width: 520px;
    height: 297px;
    overflow: hidden;
  }
  .card-front { left: 50px; background: var(--paper); color: var(--ink); }
  .card-back { left: 630px; background: var(--navy); }

  .name {
    position: absolute; left: 36px; top: 70px;
    font-size: 22px; font-weight: 700; color: var(--navy); line-height: 1;
  }
  .title {
    position: absolute; left: 36px; top: 98px;
    font-size: 14px; line-height: 18px;
  }
  .address {
    position: absolute; left: 36px; top: 120px;
    font-size: 14px; line-height: 18px;
  }
  .contact-list {
    position: absolute; list-style: none;
    font-size: 13px; line-height: 21px;
  }
  .contact-list li { display: flex; align-items: center; gap: 7px; white-space: nowrap; }
  .contact-list svg { width: 12px; height: 12px; fill: var(--navy); flex: none; }
  .phones { left: 36px; top: 146px; }
  .online { left: 140px; top: 190px; }

  .band {
    position: absolute; left: 390px; top: 0; width: 80px; height: 180px;
    background: var(--navy);
  }
  .seal-mark {
    position: absolute; left: 370px; top: 150px;
    width: 120px; height: 120px; border-radius: 50%;
    background: var(--navy);
  }
  .brand-name {
    position: absolute; left: 350px; top: 274px; width: 160px;
    text-align: center; font-size: 13px; font-weight: 700;
    color: var(--navy); letter-spacing: 1px; line-height: 16px;
  }

  .back-mark {
    position: absolute; right: 46px; bottom: 70px;
    width: 56px; height: 56px; border-radius: 50%;
    background: var(--mark);
  }
  .back-name {
    position: absolute; right: 20px; bottom: 44px; width: 108px;
    text-align: center; font-size: 11px; font-weight: 700;
    color: var(--mark); letter-spacing: 1px; line-height: 14px;
  }
</style>
</head>
<body>
  <section class="card card-front" aria-label="Business card front">
    <div class="band"></div>
    <div class="seal-mark"></div>
    <p class="brand-name">BRENVICK HOLDINGS</p>

    <h1 class="name">Dorian P.K. Halvers</h1>
    <p class="title">Managing Principal</p>
    <p class="address">418 Ostrander Ave., Suite 612 Denver, CO 80319</p>

    <ul class="contact-list phones">
      <li>
        <svg viewBox="0 0 12 12" aria-hidden="true"><path d="M1 3c0-1 1-2 2-2h6c1 0 2 1 2 2v1H8V3H4v1H1z M2 5h8l1 6H1z"/></svg>
        303-555-0192
      </li>
      <li>
        <svg viewBox="0 0 12 12" aria-hidden="true"><path d="M3 0h6a1 1 0 0 1 1 1v10a1 1 0 0 1-1 1H3a1 1 0 0 1-1-1V1a1 1 0 0 1 1-1zm0 2v7h6V2z"/></svg>
        970-555-0147
      </li>
    </ul>

    <ul class="contact-list online">
      <li>
        <svg viewBox="0 0 12 12" aria-hidden="true"><path d="M0 2h12v1L6 7 0 3z M0 4.5l6 4 6-4V10H0z"/></svg>
        Dorian@brenvickholdings.example
      </li>
      <li>
        <svg viewBox="0 0 12 12" aria-hidden="true"><circle cx="6" cy="6" r="6"/><circle cx="6" cy="4.5" r="2" fill="#f7f6f4"/><path d="M2.5 10a3.5 3 0 0 1 7 0z" fill="#f7f6f4"/></svg>
        Brenvickholdings.example
      </li>
    </ul>
  </section>

  <section class="card card-back" aria-label="Business card back">
    <div class="back-mark"></div>
    <p class="back-name">BRENVICK HOLDINGS</p>
  </section>
</body>
</html>
```